young adult fiction novel titled 'Chronicles of the Orrery - The Heron's Song'

Introduction
Hello! Attached you will find a combination of my own amateurish attempts at graphic design and also pictures that have inspired me. With the obvious exception of the ‘Crown of Embers’ and ‘Keeper of the Vales’ stuff, I have purchased the other images so they are fair game to be used (contact me if you want the hi-res versions).
I hope that by showing you these, I might be able to convey what I’m looking for in a front cover and a website. I’d just like to make a few points that might also help you understand a little better.
1. The book is called ‘The Heron’s Song’. It is a 'knights of the round table' type story so I would like
2. My concept is 12 tales, each told by a member of the zodiac. I would like the first front cover to be designed in such a way that the following 11 can be thematically linked together. The Heron’s Song is obviously the Capricorn’s tale.
3. As Capricorn is an earth sign, I would like the colour scheme to be green and brown. I would also definitely like the motto to be ‘Lift the Tide Higher’.
4. The name of the series will be ‘Chronicles of the Orrery’ and I would like this written somewhere on the front cover.
5. My Nom de Plume is going to be RM Tollingsby.
6. There is room for quirkiness in the design. The book itself is, I may say so, dryly humourous and, also, is set in the future. This allows for a slight twist on more traditional heraldry.
7. It would be nice to include a stylised zodiac wheel that could appear on all the books and the website. It would be one of the motifs that links the books together. In the story, a round table of the zodiac is set up. This is a fusion of astrology and Arthurian legend.
8. My main concern with my own design is the colouring. I was concerned that it looked a little cheap to have a single matt colour. I was thinking that some sort of texture of w/e might add a bit of quality to the design. This is not a deal breaker and, as I said, I would regard it as a safe option if the above change is made.
9. My perfect design would be more like an ACTUAL shield with elements of classic heraldry but a a subtle nod to dystopian iron dust / ember trials type art work.
Updates
Reason: I have one very strong contender but several other strong drafts on the table and want to give them a chance to improve their designs.
Target Market(s)
Western Teenagers who read fantasy novels such as KOTV, crown of embers, Milo Brackwell etc
Industry/Entity Type
Graphic Design

```html
<!DOCTYPE html>
<html lang="en">
<head>
<meta charset="utf-8">
<title>Chronicles of the Orrery - The Heron's Song</title>
<link href="https://fonts.googleapis.com/css2?family=Cinzel:wght@400;600;700&display=swap" rel="stylesheet">
<style>
  :root {
    --leather-light: #d9a066;
    --leather-mid: #c07d45;
    --leather-dark: #8a4f28;
    --ink: #4a3819;
    --ink-deep: #2f2410;
    --ring: #8a4a2f;
    --ring-dark: #5e2f1c;
    --band-green: #2f4a31;
    --band-edge: #1b2a1c;
    --series-white: #fbf4e8;
  }
  html, body {
    margin: 0;
    padding: 0;
    overflow: hidden;
    background: #ffffff;
  }
  .cover {
    position: relative;
    width: 927px;
    height: 1200px;
    overflow: hidden;
    background:
      radial-gradient(ellipse at 30% 20%, rgba(255,220,170,0.35), transparent 55%),
      radial-gradient(ellipse at 75% 65%, rgba(120,60,25,0.30), transparent 60%),
      radial-gradient(ellipse at 10% 85%, rgba(110,55,20,0.35), transparent 50%),
      radial-gradient(ellipse at 90% 15%, rgba(110,55,20,0.35), transparent 45%),
      linear-gradient(160deg, var(--leather-mid), var(--leather-light) 45%, var(--leather-mid) 80%, var(--leather-dark));
    font-family: "Cinzel", serif;
  }
  .glyph-border {
    position: absolute;
    left: 0;
    top: 32px;
    width: 927px;
    height: 70px;
    background: linear-gradient(90deg, rgba(60,35,15,0.25), rgba(60,35,15,0.35), rgba(60,35,15,0.25));
  }
  .series-name {
    position: absolute;
    top: 132px;
    left: 0;
    width: 100%;
    text-align: center;
    margin: 0;
    font-weight: 400;
    font-size: 33px;
    letter-spacing: 9px;
    color: var(--series-white);
    text-transform: uppercase;
  }
  .book-title {
    position: absolute;
    top: 262px;
    left: 0;
    width: 100%;
    margin: 0;
    text-align: center;
    color: var(--ink);
    text-transform: uppercase;
    font-weight: 600;
    text-shadow: 1px 1px 0 rgba(255,225,180,0.45), -1px -1px 1px rgba(40,25,10,0.45);
  }
  .book-title .title-article {
    display: block;
    font-size: 50px;
    line-height: 60px;
  }
  .book-title .title-main {
    display: block;
    font-size: 72px;
    line-height: 90px;
    letter-spacing: 1px;
  }
  .emblem {
    position: absolute;
    left: 0;
    top: 0;
    width: 927px;
    height: 1200px;
  }
  .author-name {
    position: absolute;
    top: 975px;
    left: 0;
    width: 100%;
    margin: 0;
    text-align: center;
    font-size: 58px;
    font-weight: 600;
    color: var(--ink);
    text-transform: uppercase;
    text-shadow: 1px 1px 0 rgba(255,225,180,0.45), -1px -1px 1px rgba(40,25,10,0.45);
  }
  .spine-band {
    position: absolute;
    left: 0;
    top: 1108px;
    width: 927px;
    height: 34px;
    background: linear-gradient(180deg, #3a5a3c, var(--band-green) 50%, #263d28);
    border-top: 3px solid var(--band-edge);
    border-bottom: 3px solid var(--band-edge);
  }
</style>
</head>
<body>
  <main class="cover">
    <div class="glyph-border" role="img" aria-label="Row of ancient script glyphs"></div>

    <p class="series-name">Chronicles of the Orrery</p>

    <h1 class="book-title">
      <span class="title-article">The</span>
      <span class="title-main">Heron’s Song</span>
    </h1>

    <svg class="emblem" viewBox="0 0 927 1200" xmlns="http://www.w3.org/2000/svg">
      <defs>
        <radialGradient id="medallion-fill" cx="50%" cy="45%" r="55%">
          <stop offset="0%" stop-color="#d9a565"/>
          <stop offset="100%" stop-color="#b9783f"/>
        </radialGradient>
        <path id="motto-arc" d="M 239 690 A 225 225 0 0 0 689 690"/>
      </defs>
      <circle cx="464" cy="690" r="175" fill="url(#medallion-fill)" role="img" aria-label="Engraved heron head emblem"/>
      <circle class="medallion-ring" cx="464" cy="690" r="186" fill="none" stroke="var(--ring)" stroke-width="22"/>
      <circle cx="464" cy="690" r="197" fill="none" stroke="var(--ring-dark)" stroke-width="2" opacity="0.6"/>
      <circle cx="464" cy="690" r="175" fill="none" stroke="var(--ring-dark)" stroke-width="2" opacity="0.6"/>
      <text class="motto" font-family="Cinzel, serif" font-size="20" font-weight="600" letter-spacing="7" fill="var(--ink-deep)">
        <textPath href="#motto-arc" startOffset="50%" text-anchor="middle">LIFT THE TIDE HIGHER</textPath>
      </text>
    </svg>

    <p class="author-name">RM Tollingsby</p>

    <div class="spine-band" role="img" aria-label="Green band with ancient script glyphs"></div>
  </main>
</body>
</html>
```